LA Billboard Project for Brisk Lending

We are running three different billboards around LA, and we need someone to take the mock-ups I've created and bring this campaign to life. Whatever wording is on the mock-ups should stay the same in the ads you create, but feel free to get creative with layout and style. I've attached our mock-ups, our style guide, our logo, and the necessary specs for the billboards. If you have any questions, feel free to reach out!

```html
<!DOCTYPE html>
<html lang="en">
<head>
<meta charset="utf-8">
<title>Brisk Lending — Billboard</title>
<link rel="stylesheet" href="https://fonts.googleapis.com/css2?family=Hind:wght@500;600&display=swap">
<style>
  :root {
    --page: #ffffff;
    --board-dark: #02060d;
    --board-navy: #0a2a4a;
    --brand-cyan: #16bcd6;
    --headline-yellow: #f4dd00;
    --text-white: #ffffff;
    --photo-blue: #1d3c5c;
    --photo-amber: #8a6a4c;
    --photo-night: #0c1622;
  }
  * { margin: 0; padding: 0; box-sizing: border-box; }
  html, body {
    width: 768px;
    height: 1200px;
    overflow: hidden;
    background: var(--page);
    font-family: "Hind", sans-serif;
  }
  .canvas {
    position: relative;
    width: 768px;
    height: 1200px;
    display: flex;
    align-items: center;
    justify-content: center;
  }
  .billboard {
    position: relative;
    width: 700px;
    height: 467px;
    overflow: hidden;
    background: linear-gradient(160deg, var(--board-navy) 0%, var(--board-dark) 55%, var(--board-dark) 100%);
  }
  .billboard__photo {
    position: absolute;
    top: 0;
    right: 0;
    width: 484px;
    height: 100%;
    background:
      radial-gradient(ellipse at 75% 8%, rgba(180, 205, 225, 0.55) 0%, rgba(29, 60, 92, 0) 45%),
      linear-gradient(172deg, var(--photo-blue) 0%, var(--photo-night) 38%, var(--photo-amber) 62%, var(--photo-night) 78%, #161a22 100%);
  }
  .billboard__fade {
    position: absolute;
    top: 0;
    left: 200px;
    width: 200px;
    height: 100%;
    background: linear-gradient(90deg, var(--board-dark) 0%, rgba(2, 6, 13, 0) 100%);
  }
  .billboard__copy {
    position: absolute;
    top: 0;
    left: 0;
    width: 340px;
    height: 100%;
    padding: 50px 0 0 46px;
  }
  .brand-name {
    font-weight: 600;
    font-size: 40px;
    line-height: 1;
    color: var(--brand-cyan);
    letter-spacing: -0.5px;
  }
  .headline {
    margin-top: 80px;
    font-weight: 600;
    font-size: 29px;
    line-height: 1.1;
    color: var(--headline-yellow);
  }
  .subline {
    margin-top: 10px;
    font-weight: 600;
    font-size: 21px;
    line-height: 1.3;
    color: var(--text-white);
  }
  .web-address {
    position: absolute;
    left: 46px;
    bottom: 40px;
    font-weight: 600;
    font-size: 21px;
    color: var(--text-white);
    letter-spacing: 0.2px;
  }
</style>
</head>
<body>
  <main class="canvas">
    <section class="billboard">
      <div class="billboard__photo" role="img" aria-label="Night highway with long-exposure light trails of traffic under a blurred city skyline"></div>
      <div class="billboard__fade"></div>
      <div class="billboard__copy">
        <div class="brand-name">Brisk Lending</div>
        <h1 class="headline">Traffic is a mess.</h1>
        <p class="subline">Your mortgage<br>doesn't have to be.</p>
      </div>
      <div class="web-address">BRISKLENDING.COM</div>
    </section>
  </main>
</body>
</html>
```